Quarvel Drips

We are making a lable for a jar or a cellophane package for CBD&CBG gummies.

My Idea is an astronaut on the moon with a Hollywood billboard with the brand name. Put a goldchain on the person with a Hemp Leaf medallion. Thats my only Idea but I need to see yours.

Target Market(s)

Every adult over 21

Requirements
Must have
• I included 2 methods to package gummies (2 example of other's product). An idea only, the gummies could be astronauts instead of bears.

```html
<!DOCTYPE html>
<html lang="en">
<head>
<meta charset="utf-8">
<title>CBD Gummies Pouch Label</title>
<link href="https://fonts.googleapis.com/css2?family=Bungee&family=Montserrat:wght@500;800&family=Oswald:wght@500&display=swap" rel="stylesheet">
<style>
  :root {
    --backdrop: #a39d9d;
    --night-purple: #3e2448;
    --band-purple: #3a2144;
    --window-white: #ffffff;
    --planet-blue: #2a9ccc;
    --planet-deep: #1f7fae;
    --sign-orange: #ef6a1f;
    --sign-red: #c9261a;
    --bulb-yellow: #ffe79a;
    --title-yellow: #f6ec83;
    --title-shadow: #d8321e;
    --ink: #111111;
    --paper-text: #f3eef5;
  }
  html, body {
    margin: 0;
    width: 1200px;
    height: 1200px;
    overflow: hidden;
    background: var(--backdrop);
  }
  .canvas {
    position: relative;
    width: 1200px;
    height: 1200px;
  }
  .label {
    position: absolute;
    left: 210px;
    top: 50px;
    width: 780px;
    height: 1099px;
    display: block;
  }
  .title-text {
    font-family: "Bungee", "Impact", sans-serif;
    fill: var(--title-yellow);
    stroke: var(--title-shadow);
    stroke-width: 1.5;
    paint-order: stroke;
  }
  .title-depth {
    font-family: "Bungee", "Impact", sans-serif;
    fill: var(--title-shadow);
  }
  .window-note {
    font-family: "Montserrat", sans-serif;
    font-weight: 800;
    font-size: 19px;
    fill: var(--ink);
  }
  .dose-main {
    font-family: "Montserrat", sans-serif;
    font-weight: 800;
    font-size: 30px;
    fill: var(--ink);
  }
  .dose-note {
    font-family: "Montserrat", sans-serif;
    font-weight: 500;
    font-size: 11px;
    fill: var(--ink);
  }
  .footer-text {
    font-family: "Montserrat", sans-serif;
    font-weight: 500;
    font-size: 13px;
    fill: var(--paper-text);
  }
  .net-weight {
    font-family: "Oswald", sans-serif;
    font-weight: 500;
    font-size: 17px;
    letter-spacing: 1px;
    fill: var(--paper-text);
  }
</style>
</head>
<body>
<main class="canvas">
  <svg class="label" viewBox="0 0 660 930" xmlns="http://www.w3.org/2000/svg">
    <defs>
      <linearGradient id="astronautTone" x1="0" y1="0" x2="1" y2="1">
        <stop offset="0" stop-color="#e9e9e9"/>
        <stop offset="0.55" stop-color="#8a8a8a"/>
        <stop offset="1" stop-color="#2a2a2a"/>
      </linearGradient>
    </defs>

    <!-- background -->
    <rect class="label-base" width="660" height="930" fill="var(--night-purple)"/>

    <!-- transparent window area -->
    <path class="clear-window" d="M0 270 Q330 240 660 320 L660 575 Q320 620 0 725 Z" fill="var(--window-white)"/>

    <!-- planet band -->
    <path class="planet-band" d="M0 725 Q320 620 660 575 L660 855 L0 855 Z" fill="var(--planet-blue)"/>
    <path class="planet-shade" d="M0 800 Q340 700 660 660 L660 855 L0 855 Z" fill="var(--planet-deep)" opacity="0.45"/>

    <!-- bottom band -->
    <rect class="footer-band" x="0" y="853" width="660" height="77" fill="var(--band-purple)"/>

    <!-- marquee sign -->
    <g class="marquee-sign">
      <path d="M48 150 Q48 128 70 128 L178 128 Q200 40 320 30 Q440 40 462 128 L570 128 Q592 128 592 150 L592 340 Q592 362 570 362 L70 362 Q48 362 48 340 Z"
            fill="var(--sign-orange)" stroke="var(--sign-red)" stroke-width="4"/>
      <path d="M48 150 Q48 128 70 128 L178 128 Q200 40 320 30 Q440 40 462 128 L570 128 Q592 128 592 150 L592 340 Q592 362 570 362 L70 362 Q48 362 48 340 Z"
            fill="none" stroke="var(--bulb-yellow)" stroke-width="7" stroke-linecap="round" stroke-dasharray="0 17" transform="translate(0 0)" opacity="0.95"/>
      <path d="M74 158 L198 158 Q220 70 320 62 Q420 70 442 158 L566 158 L566 334 L74 334 Z"
            fill="var(--window-white)" stroke="var(--sign-red)" stroke-width="3"/>
      <text class="title-depth" x="314" y="187" font-size="76" text-anchor="middle">CBD</text>
      <text class="title-text" x="310" y="182" font-size="76" text-anchor="middle">CBD</text>
      <text class="title-depth" x="324" y="294" font-size="78" text-anchor="middle">GUMMIES</text>
      <text class="title-text" x="320" y="289" font-size="78" text-anchor="middle">GUMMIES</text>
    </g>

    <!-- astronaut illustration area -->
    <path class="astronaut-art" role="img" aria-label="Illustration of an astronaut in a spacesuit wearing a gold chain with a hemp leaf medallion"
          d="M355 300 L470 290 Q560 300 580 380 L600 470 Q650 560 640 700 L620 930 L300 930 L310 780 Q260 740 260 640 Q280 520 360 470 Z"
          fill="url(#astronautTone)"/>

    <!-- window note -->
    <text class="window-note" x="82" y="514">TRANSPARENT</text>

    <!-- dosage -->
    <text class="dose-main" x="40" y="812">CBD 75MG</text>
    <text class="dose-note" x="140" y="830" text-anchor="middle">APPROX PER POUNCH</text>
    <text class="dose-note" x="140" y="842" text-anchor="middle">(approx 5.5 mg per gummy)</text>

    <!-- footer -->
    <text class="footer-text" x="138" y="877" text-anchor="middle">DIETARY SUPPLEMENT</text>
    <text class="footer-text" x="138" y="894" text-anchor="middle">PROUDLY MADE IN THE USA</text>
    <text class="net-weight" x="138" y="918" text-anchor="middle">NET.WT.40G</text>
  </svg>
</main>
</body>
</html>
```